AMBER AND STONE WEB

We need a home design in wordpress, we have now a web but we would like to improve it. Our current web is www.amberandstonevillas.example Our business is holliday rental of villas in Ibiza. Our guest must know that we are a reliable company, professional and with experience and good reviews. We want them to click in our reservation engine: https://bookings.amberandstonevillas.example/en/ and make reservation in our website. We would also like to say that all the properties that we have are just us who commercialize so we have best price available. Many people are going to see our villas in staylister.example and look to our website to make a reservation with us so we need to show them that they are at the right place and click at our link to our reservation engine. What make us special is that we are a local company, we are from Ibiza, Our guests are always received in person by the Amber and Stone Villas team. You will enjoy extensive tourist information when you check in and during the entire stay. You will be attended by ChatLoop and calls, always happy to help so that you have a happy and fun stay! Our guest stay is better than in hotel as they have more spece, private swiming pool, private garden, barbeque ... To rent a villa is the best way to stay in Ibiza. We also have a promotional video: https://vidshare.example/Qm7tLp2Xz9A Let our philosophy be shown, we think that coming on holiday to Ibiza implies seeing the nature that we have in Ibiza, hence our name AMBER AND STONE, like the pins that almost touch the sea in Ibiza, or the posidonea meadows where the intense green of the seaweed and the blue of the sea. We are aware of the environment, and we love Ibiza. For us, the client who visits Ibiza, should rent a car, go around the island, eat in a restaurant one day in front of the sea, is a night of partying to the discs, go shopping, visit the ancient heritage of Umanity, make some aquatic sport, enjoy the pool, those are for us Ibiza.

Target Market(s)

Europe, people from Holand, UK, Germany, France, Spain ...

Industry/Entity Type

Tourism

Colors

Designer to choose colors to be used in the design.

Requirements
Must have
• Pictures of Ibiza.
Nice to have
• Our name Amber and Stone Villas is beacuse in Ibiza there is forest that almost touch the watter of the Mediterranean sea, so you can see green of the forest and blue of the sea and the sky. And also beacause under the watter of the sea there is a plant called Posidonia that is also green please see the picture of posidonia.

```html
<!DOCTYPE html>
<html lang="en">
<head>
<meta charset="utf-8">
<title>Amber and Stone Villas – Ibiza</title>
<link rel="stylesheet" href="https://fonts.googleapis.com/css2?family=Playfair+Display:ital,wght@0,400;0,500;1,400&family=Work+Sans:wght@400;500&display=swap">
<style>
:root{
  --green:#a6b93a;
  --green-dark:#8fa12c;
  --ink:#222222;
  --text:#555555;
  --muted:#9a9a9a;
  --sky-band:#e9f5fe;
  --grey-box:#eef0f1;
  --line:#e2e2e2;
  --white:#ffffff;
}
*{box-sizing:border-box;margin:0;padding:0}
html,body{width:1200px;height:3247px;overflow:hidden;background:var(--white)}
body{font-family:"Work Sans",Arial,sans-serif;color:var(--text);font-size:9px}
.page{position:relative;width:1200px;height:3247px;overflow:hidden}
.abs{position:absolute}
.serif{font-family:"Playfair Display",Georgia,serif}
.caps{text-transform:uppercase;letter-spacing:1.6px}

/* header */
.site-header{left:0;top:0;width:1200px;height:57px;border-bottom:1px solid #eee;background:var(--white)}
.header-phone{left:234px;top:19px;font-size:9px;color:var(--text);display:flex;align-items:center;gap:6px}
.header-menu{left:351px;top:19px;font-size:8px;color:var(--text);text-decoration:underline;letter-spacing:.8px}
.brand{left:0;width:1200px;top:17px;text-align:center;font-family:"Work Sans",sans-serif;font-size:15px;font-weight:500;color:var(--green);letter-spacing:.5px}
.btn-green{background:var(--green);color:var(--white);font-size:8px;letter-spacing:1.8px;text-transform:uppercase;display:flex;align-items:center;justify-content:center}
.header-book{left:813px;top:14px;width:87px;height:23px}

/* hero */
.photo{display:block}
.hero-photo{left:0;top:57px;width:1200px;height:508px;background:linear-gradient(180deg,#4a8fe0 0%,#8cbdf0 14%,#1450b4 32%,#1a5dbf 55%,#2a9ab6 72%,#5e8d3a 86%,#3f7a2a 100%)}
.hero-card{left:232px;top:426px;width:483px;height:204px;background:var(--white)}
.hero-title{left:278px;top:452px;font-size:28px;line-height:33px;letter-spacing:3.6px;color:var(--ink);font-weight:400}
.hero-text{left:278px;top:527px;width:340px;font-size:8px;line-height:16px;color:var(--text)}
.btn-outline{border:1.5px solid var(--ink);font-size:8px;letter-spacing:1.8px;text-transform:uppercase;color:var(--ink);display:flex;align-items:center;padding-left:14px}
.arrow{position:absolute;right:-12px;top:50%;transform:translateY(-50%)}
.hero-tour{left:277px;top:577px;width:157px;height:31px}

.booking{left:715px;top:426px;width:251px;height:182px;background:var(--green);color:var(--white)}
.booking h3{position:absolute;left:19px;top:16px;font-family:"Playfair Display",serif;font-weight:400;font-size:11px;letter-spacing:1px}
.field-label{position:absolute;font-size:6.5px;letter-spacing:.8px;text-transform:uppercase}
.field{position:absolute;background:var(--white);height:26px;color:var(--text);font-size:6.5px;display:flex;align-items:center;padding-left:8px;justify-content:space-between;padding-right:7px}
.booking-link{position:absolute;left:19px;top:151px;font-size:7.5px;letter-spacing:1.2px;text-decoration:underline;display:flex;align-items:center;gap:8px}

/* properties */
.section-title{left:0;width:1200px;text-align:center;font-family:"Playfair Display",serif;font-size:19px;letter-spacing:2.6px;color:var(--ink)}
.villa{top:731px;width:169px;height:145px}
.villa-label{position:absolute;left:50%;transform:translateX(-50%);bottom:0;background:var(--white);font-size:7.5px;letter-spacing:1.6px;text-transform:uppercase;color:var(--ink);padding:4px 10px 2px;white-space:nowrap}
.villa-label.active{background:var(--green);color:var(--white)}
.view-villas{left:517px;top:923px;width:156px;height:31px}

/* speciality */
.specialty-band{left:0;top:1027px;width:1200px;height:470px;background:var(--sky-band)}
.specialty{top:1165px;width:150px;text-align:center}
.specialty .name{margin-top:12px;font-size:9px;letter-spacing:1.6px;text-transform:uppercase;color:var(--ink)}
.specialty .detail{margin-top:7px;font-size:6.5px;letter-spacing:1.3px;text-transform:uppercase;color:var(--muted)}
.specialty .detail.active{color:var(--ink);text-decoration:underline;font-weight:500}
.beach-photo{left:296px;top:1318px;width:607px;height:343px;background:linear-gradient(180deg,#5f9ce0 0%,#b9d6f2 30%,#3f91c9 38%,#e9dcc6 48%,#e6d2b2 100%)}
.feature-card{left:487px;top:1382px;width:226px;height:214px;background:var(--white);text-align:center}
.feature-card h2{margin-top:28px;font-family:"Playfair Display",serif;font-weight:400;font-size:25px;line-height:29px;letter-spacing:2.4px;color:var(--ink)}
.feature-card p{margin:18px auto 0;width:200px;font-size:7px;line-height:12px}
.feature-book{left:517px;top:1539px;width:156px;height:30px;justify-content:flex-start;padding-left:14px}

/* testimonial */
.testimonial-mark{left:592px;top:1744px;width:16px;height:16px;border-radius:50%;background:var(--green)}
.quote{left:330px;top:1806px;width:540px;text-align:center;font-family:"Playfair Display",serif;font-style:italic;font-size:14px;line-height:20px;letter-spacing:.9px;color:var(--ink)}
.quote-author{left:0;width:1200px;top:1893px;text-align:center;font-family:"Playfair Display",serif;font-style:italic;font-size:13px;letter-spacing:1.4px;color:var(--green)}
.dots{left:574px;top:1945px;display:flex;gap:7px}
.dots span{width:7px;height:7px;border-radius:50%;background:#c8c8c8}
.dots span.on{background:#666}

/* video */
.coast-photo{left:0;top:2312px;width:1200px;height:418px;background:linear-gradient(180deg,#2e7fd8 0%,#7db3ea 20%,#1f5fb8 38%,#1f8fb0 58%,#4aa6a2 70%,#4f7a37 86%,#3b6a2a 100%)}
.video-box{left:234px;top:2027px;width:732px;height:360px;background:var(--grey-box)}
.video-title{left:278px;top:2108px;font-size:25px;line-height:32px;letter-spacing:3px;color:var(--ink);font-weight:400}
.video-text{left:278px;top:2222px;width:390px;font-size:8px;line-height:16px}
.view-video{left:755px;top:2154px;width:156px;height:31px}
.coast-title{left:278px;top:2516px;font-size:25px;letter-spacing:3px;color:var(--white);font-weight:400}
.coast-text{left:278px;top:2560px;width:400px;font-size:8px;line-height:14px;color:var(--white)}

/* newsletter */
.newsletter-sub{left:0;width:1200px;top:2834px;text-align:center;font-size:8px;color:var(--ink)}
.newsletter-form{left:487px;top:2865px;width:226px;height:32px;border:1px solid var(--green);display:flex}
.newsletter-form span{flex:1;font-size:7.5px;letter-spacing:.8px;display:flex;align-items:center;padding-left:11px;color:var(--text)}
.newsletter-form b{width:32px;background:var(--green);display:flex;align-items:center;justify-content:center}
.to-top{left:1027px;top:2923px;width:32px;height:31px;background:#1e88e5;display:flex;align-items:center;justify-content:center}
.footer-rule{left:234px;top:2971px;width:732px;height:1px;background:var(--line)}

/* footer */
.footer-book{left:234px;top:3048px;width:157px;height:30px;justify-content:flex-start;padding-left:14px}
.copyright{left:234px;top:3121px;font-size:8px;color:var(--ink)}
.footer-heading{font-family:"Playfair Display",serif;font-size:11px;letter-spacing:1.5px;color:var(--ink)}
.footer-list{list-style:none;margin-top:13px;font-size:7.5px;letter-spacing:.8px;line-height:15.6px;text-transform:uppercase;color:var(--text)}
.contact-text{margin-top:14px;font-size:7.5px;line-height:15.6px;letter-spacing:.5px;color:var(--text)}
.contact-line{display:flex;align-items:center;gap:6px;font-size:7.5px;line-height:17px}
.social{display:grid;grid-template-columns:repeat(3,20px);gap:13px 14px}
.social span{width:20px;height:20px;background:#8c8c8c}
.social span.on{background:var(--green)}
.legal{left:797px;top:3126px;font-size:7.5px;color:var(--ink)}
</style>
</head>
<body>
<div class="page">

  <header class="site-header abs">
    <div class="header-phone abs">
      <svg width="10" height="10" viewBox="0 0 10 10"><path d="M2 1l2 2-1 1.2c.6 1.2 1.5 2.1 2.8 2.8L7 6l2 2-1.2 1.3C4.6 9 1 5.4.7 2.2z" fill="none" stroke="#6a9a5a" stroke-width=".8"/></svg>
      +34 600 000 111
    </div>
    <div class="header-menu abs">ALL PROPERTIES &nbsp;&nbsp;⌄</div>
    <div class="brand abs">AMBER AND STONE</div>
    <div class="header-book abs btn-green">Book Now</div>
    <svg class="abs" style="left:916px;top:20px" width="10" height="10" viewBox="0 0 10 10"><circle cx="4" cy="4" r="3" fill="none" stroke="#222" stroke-width="1.5"/><path d="M6.3 6.3L9 9" stroke="#222" stroke-width="1.6"/></svg>
    <svg class="abs" style="left:952px;top:19px" width="13" height="11" viewBox="0 0 13 11"><path d="M0 1.5h13M0 5.5h13M0 9.5h13" stroke="#222" stroke-width="1.8"/></svg>
  </header>

  <div class="hero-photo abs photo" role="img" aria-label="Photo of an Ibiza cove with pine-covered cliffs, sailing boats on deep blue sea and a small sandy beach"></div>
  <div class="hero-card abs"></div>
  <h1 class="hero-title abs serif">THE BEST OPTION TO<br>STAY IN IBIZA</h1>
  <p class="hero-text abs">Amber and Stone Villas is a company specialized in offering its clients accommodation in Villas on the countryside of Ibiza.</p>
  <div class="hero-tour abs btn-outline">Take a Tour
    <svg class="arrow" width="30" height="10" viewBox="0 0 30 10"><path d="M0 5h28M24 1l4 4-4 4" fill="none" stroke="#222" stroke-width="1.2"/></svg>
  </div>

  <form class="booking abs">
    <h3>Book Your Room</h3>
    <span class="field-label" style="left:19px;top:43px">Arrival</span>
    <span class="field-label" style="left:130px;top:43px">Departure</span>
    <div class="field" style="left:19px;top:55px;width:103px">08 MAY 2018 <span>▦</span></div>
    <div class="field" style="left:129px;top:55px;width:103px">10 MAY 2018 <span>▦</span></div>
    <span class="field-label" style="left:19px;top:95px">Rooms</span>
    <span class="field-label" style="left:130px;top:95px">Adults</span>
    <span class="field-label" style="left:185px;top:95px">Child</span>
    <div class="field" style="left:19px;top:107px;width:103px">1 <span>⌄</span></div>
    <div class="field" style="left:129px;top:107px;width:48px">2 <span>⌄</span></div>
    <div class="field" style="left:184px;top:107px;width:48px">0 <span>⌄</span></div>
    <div class="booking-link">CHECK AVAILABILITY
      <svg width="18" height="8" viewBox="0 0 18 8"><path d="M0 4h16M13 1l3 3-3 3" fill="none" stroke="#fff" stroke-width="1.2"/></svg>
    </div>
  </form>

  <h2 class="section-title abs" style="top:676px">All Properties</h2>
  <div class="villa abs photo" style="left:234px;background:linear-gradient(160deg,#f1ece4,#d8cbb6 60%,#a68a63)" role="img" aria-label="Bright villa bedroom with white bedding and wooden furniture"><span class="villa-label">Villa Can Serra</span></div>
  <div class="villa abs photo" style="left:422px;background:linear-gradient(160deg,#f3f2ef,#dcd8d0 55%,#8d7658)" role="img" aria-label="Villa bedroom with twin beds and a window onto the garden"><span class="villa-label active">Villa Can Roure</span></div>
  <div class="villa abs photo" style="left:609px;background:linear-gradient(160deg,#c9a27a,#4e6c9a 55%,#8a6a48)" role="img" aria-label="Villa lounge with blue sofas, wooden beams and dining table"><span class="villa-label">Villa Can Olivera</span></div>
  <div class="villa abs photo" style="left:797px;background:linear-gradient(160deg,#f2f1ee,#dedbd5 55%,#9c9994)" role="img" aria-label="Bright villa living room with white sofas and chandelier"><span class="villa-label">Villa Les Tres Pinedes</span></div>
  <div class="view-villas abs btn-outline">View All Villas
    <svg class="arrow" width="30" height="10" viewBox="0 0 30 10"><path d="M0 5h28M24 1l4 4-4 4" fill="none" stroke="#222" stroke-width="1.2"/></svg>
  </div>

  <section class="specialty-band abs"></section>
  <h2 class="section-title abs" style="top:1097px">Discover our Speciality</h2>
  <svg class="abs" style="left:138px;top:1185px" width="18" height="40" viewBox="0 0 18 40"><path d="M17 1L1 20l16 19" fill="none" stroke="#888" stroke-width="1"/></svg>
  <svg class="abs" style="left:1043px;top:1185px" width="18" height="40" viewBox="0 0 18 40"><path d="M1 1l16 19L1 39" fill="none" stroke="#888" stroke-width="1"/></svg>

  <div class="specialty abs" style="left:278px">
    <svg width="60" height="28" viewBox="0 0 60 28"><rect x="2" y="6" width="56" height="18" fill="none" stroke="#444" stroke-width="1.3"/><rect x="8" y="12" width="18" height="6" fill="#444"/><rect x="34" y="12" width="18" height="6" fill="#444"/><path d="M2 24v3M58 24v3" stroke="#444" stroke-width="1.3"/></svg>
    <div class="name">Accommodation</div><div class="detail">Details</div>
  </div>
  <div class="specialty abs" style="left:463px">
    <svg width="36" height="28" viewBox="0 0 36 28"><path d="M6 2h24M6 6h24M6 10h24" stroke="#444" stroke-width="1.3"/><path d="M3 14h30c0 7-6 12-15 12S3 21 3 14z" fill="#444"/></svg>
    <div class="name">Dining</div><div class="detail active">Details</div>
  </div>
  <div class="specialty abs" style="left:633px">
    <svg width="54" height="30" viewBox="0 0 54 30"><circle cx="11" cy="19" r="9" fill="none" stroke="#444" stroke-width="1.5"/><circle cx="43" cy="19" r="9" fill="none" stroke="#444" stroke-width="1.5"/><path d="M11 19l9-12h15l8 12M20 7l7 12 8-12M18 4h6M33 4h5" fill="none" stroke="#444" stroke-width="1.5"/></svg>
    <div class="name">Bicycles Rental</div><div class="detail">Details</div>
  </div>
  <div class="specialty abs" style="left:809px">
    <svg width="34" height="32" viewBox="0 0 34 32"><path d="M3 2h28L17 16zM17 16v14M10 30h14" fill="none" stroke="#444" stroke-width="1.4"/><circle cx="26" cy="5" r="4" fill="none" stroke="#444" stroke-width="1.2"/></svg>
    <div class="name">Bar</div><div class="detail">Details</div>
  </div>

  <div class="beach-photo abs photo" role="img" aria-label="Wooden sun loungers on a white sandy beach under a blue sky with clouds"></div>
  <div class="feature-card abs">
    <h2>Villas &amp;<br>Countryside</h2>
    <p>Our guests enjoy the rural Ibiza, tranquility, relax, private pool, close to dream beaches</p>
  </div>
  <div class="feature-book abs btn-green">Book Now
    <svg class="arrow" width="30" height="10" viewBox="0 0 30 10"><path d="M0 5h28M24 1l4 4-4 4" fill="none" stroke="#a6b93a" stroke-width="1.2"/></svg>
  </div>

  <div class="testimonial-mark abs" aria-hidden="true"></div>
  <blockquote class="quote abs">“The Hotel is simply amazing. The subtle luxury of refined simplicity, uncluttered and unpretentious. Very private and the staff is an attentive and discreet.”</blockquote>
  <div class="quote-author abs">Elena Varga</div>
  <div class="dots abs"><span></span><span></span><span class="on"></span><span></span></div>

  <div class="coast-photo abs photo" role="img" aria-label="Panoramic view of an Ibiza bay with turquoise water, a busy beach and pine-covered hills"></div>
  <div class="video-box abs"></div>
  <h2 class="video-title abs serif">Have you ever seen this<br>ibiza face? watch this</h2>
  <p class="video-text abs">The maximum distances of the island are 41 kilometers from north to south and 15 kilometers from east to west, we always recommend renting a car. Enjoy the freedom to go where you prefer, without depending on schedules or public transportation.</p>
  <div class="view-video abs btn-outline">View Video
    <svg class="arrow" width="30" height="10" viewBox="0 0 30 10"><path d="M0 5h28M24 1l4 4-4 4" fill="none" stroke="#222" stroke-width="1.2"/></svg>
  </div>
  <h2 class="coast-title abs serif">The Best Way To Stay In Ibiza!</h2>
  <p class="coast-text abs">Every day can be a different experience, beach, restaurant, flea market, disco, hiking, kayaking, horseback riding, shopping, history, boat ride! There is a lot of variety for all budgets!</p>

  <h2 class="section-title abs" style="top:2800px">Amber &amp; Stone Villas Newsletter</h2>
  <p class="newsletter-sub abs">Receive email newsletters and regular updates</p>
  <div class="newsletter-form abs"><span>ENTER EMAIL</span><b><svg width="12" height="9" viewBox="0 0 12 9"><rect x=".5" y=".5" width="11" height="8" fill="none" stroke="#fff"/><path d="M.5.5L6 5l5.5-4.5" fill="none" stroke="#fff"/></svg></b></div>
  <div class="to-top abs"><svg width="16" height="10" viewBox="0 0 16 10"><path d="M1 9l7-7 7 7" fill="none" stroke="#fff" stroke-width="2"/></svg></div>
  <div class="footer-rule abs"></div>

  <footer>
    <div class="footer-book abs btn-green">Book Now
      <svg class="arrow" width="30" height="10" viewBox="0 0 30 10"><path d="M0 5h28M24 1l4 4-4 4" fill="none" stroke="#a6b93a" stroke-width="1.2"/></svg>
    </div>
    <p class="copyright abs">© 2019 Amber &amp; Stone Villas | All right reserved.</p>

    <nav class="abs" style="left:484px;top:3043px">
      <div class="footer-heading">Sitemap</div>
      <ul class="footer-list"><li>Home</li><li>Experience</li><li>All Properties</li><li>About Us</li><li>Contact Us</li><li>Book</li></ul>
    </nav>

    <address class="abs" style="left:609px;top:3043px;font-style:normal">
      <div class="footer-heading">Contact</div>
      <div class="contact-text">Amber &amp; Stone Villas<br>CARRER DELS PINS, 8,<br>VILA NOVA, 07999,<br>IBIZA, Spain</div>
      <div style="margin-top:14px">
        <div class="contact-line"><svg width="10" height="10" viewBox="0 0 10 10"><path d="M2 1l2 2-1 1.2c.6 1.2 1.5 2.1 2.8 2.8L7 6l2 2-1.2 1.3C4.6 9 1 5.4.7 2.2z" fill="none" stroke="#a6b93a" stroke-width=".8"/></svg>+34 600 000 111</div>
        <div class="contact-line"><svg width="11" height="8" viewBox="0 0 11 8"><rect x=".5" y=".5" width="10" height="7" fill="none" stroke="#a6b93a" stroke-width=".8"/><path d="M.5.5L5.5 4.5 10.5.5" fill="none" stroke="#a6b93a" stroke-width=".8"/></svg>reservas@amberandstonevillas.example</div>
      </div>
    </address>

    <div class="social abs" style="left:797px;top:3046px" aria-label="Social network links">
      <span class="on"></span><span></span><span></span><span></span><span></span>
    </div>
    <p class="legal abs">Privacy | Legal | Terms | Cookies</p>
  </footer>

</div>
</body>
</html>
```